BrambleWorks business card

Looking for business card design that supports our company/software values. We have 2 logo designs at the moment but open to change if you think you can enhance the brand. Check out website www.brambleworks.com.au.

Target Market(s)

Education

Contact Information for Business Card

Name, title, mobile, email and website

Font styles to use
Sans Serif

Colors

Designer to choose colors to be used in the design.

Requirements
Must have
• BrambleWorks logo with tree and tagline on rear side with dark grey background colour

```html
<!DOCTYPE html>
<html lang="en">
<head>
<meta charset="utf-8">
<title>BrambleWorks Business Card</title>
<link rel="stylesheet" href="https://fonts.googleapis.com/css2?family=Ubuntu:wght@400;500&display=swap">
<style>
  :root {
    --backdrop: #ececec;
    --card-dark: #4a4a4a;
    --card-dark-glow: #545454;
    --card-light: #ffffff;
    --text-light: #e8e8e8;
    --text-dark: #4a4a4a;
    --text-body: #444444;
    --accent-green: #3d6b24;
    --mark-light: #d9d9d9;
    --mark-dark: #555555;
  }
  * { margin: 0; padding: 0; box-sizing: border-box; }
  html, body {
    width: 1200px; height: 900px; overflow: hidden;
    background: var(--backdrop);
    font-family: "Ubuntu", Arial, sans-serif;
  }
  .stage { position: relative; width: 1200px; height: 900px; }
  .card {
    position: absolute; left: 289px; width: 623px; height: 355px; overflow: hidden;
  }
  .card--front { top: 71px; background: var(--card-dark); }
  .card--back { top: 474px; background: var(--card-light); }

  .card__backdrop {
    position: absolute; inset: 0;
    background:
      radial-gradient(ellipse 300px 230px at 78% 45%, var(--card-dark-glow) 0%, rgba(84,84,84,0) 100%),
      radial-gradient(ellipse 220px 170px at 30% 45%, var(--card-dark-glow) 0%, rgba(84,84,84,0) 100%);
  }

  .brand { position: absolute; display: flex; align-items: center; }
  .brand__dot { border-radius: 50%; flex: none; }
  .brand__text { display: flex; flex-direction: column; }
  .brand__name { font-weight: 400; line-height: 1; }
  .brand__tagline { border-top: 1px solid; font-weight: 400; }

  .card--front .brand { left: 187px; top: 140px; }
  .card--front .brand__dot { width: 80px; height: 80px; background: var(--mark-light); margin-right: 14px; }
  .card--front .brand__name { font-size: 37px; color: var(--text-light); padding-bottom: 7px; }
  .card--front .brand__tagline { font-size: 17px; color: var(--text-light); border-color: var(--text-light); padding: 5px 0 0 5px; }

  .card--back .brand { left: 80px; top: 50px; }
  .card--back .brand__dot { width: 56px; height: 56px; background: var(--mark-dark); margin-right: 12px; }
  .card--back .brand__name { font-size: 28px; color: var(--text-dark); padding-bottom: 5px; }
  .card--back .brand__tagline { font-size: 13px; color: var(--text-dark); border-color: var(--text-dark); padding: 4px 0 0 4px; }

  .person { position: absolute; right: 35px; top: 142px; text-align: right; }
  .person__name { font-size: 22px; font-weight: 500; color: var(--accent-green); }
  .person__title { font-size: 15px; color: var(--text-body); margin-top: 1px; }

  .divider { position: absolute; left: 42px; right: 39px; top: 207px; height: 2px; background: var(--accent-green); }

  .contacts { position: absolute; left: 38px; top: 231px; list-style: none; }
  .contacts li { display: flex; align-items: center; height: 27.5px; font-size: 16.5px; color: var(--text-body); }
  .contacts svg { width: 18px; height: 18px; margin-right: 14px; fill: var(--accent-green); }

  .address { position: absolute; right: 36px; top: 264px; text-align: right; font-size: 16.5px; line-height: 25px; color: var(--text-body); font-style: normal; letter-spacing: 0.2px; }
</style>
</head>
<body>
<main class="stage">
  <section class="card card--front" aria-label="Card front">
    <div class="card__backdrop" role="img" aria-label="Large faint tree illustration filling the card background"></div>
    <div class="brand">
      <span class="brand__dot"></span>
      <div class="brand__text">
        <span class="brand__name">BrambleWorks</span>
        <span class="brand__tagline">Student Success Platform</span>
      </div>
    </div>
  </section>

  <section class="card card--back" aria-label="Card back">
    <div class="brand">
      <span class="brand__dot"></span>
      <div class="brand__text">
        <span class="brand__name">BrambleWorks</span>
        <span class="brand__tagline">Student Success Platform</span>
      </div>
    </div>

    <div class="person">
      <p class="person__name">Daniel Carter</p>
      <p class="person__title">CEO | Founder</p>
    </div>

    <div class="divider"></div>

    <ul class="contacts">
      <li>
        <svg viewBox="0 0 24 24" aria-hidden="true"><path d="M6.6 10.8a15.1 15.1 0 0 0 6.6 6.6l2.2-2.2c.3-.3.7-.4 1-.2 1.1.4 2.3.6 3.6.6.6 0 1 .4 1 1V20c0 .6-.4 1-1 1A17 17 0 0 1 3 4c0-.6.4-1 1-1h3.5c.6 0 1 .4 1 1 0 1.3.2 2.5.6 3.6.1.3 0 .7-.2 1z"/></svg>
        0 198 765 4321
      </li>
      <li>
        <svg viewBox="0 0 24 24" aria-hidden="true"><path d="M2 6h20v2.2l-10 6-10-6z"/><path d="M2 10.5l10 6 10-6V19H2z"/></svg>
        hello@brambleworks.com.au
      </li>
      <li>
        <svg viewBox="0 0 24 24" aria-hidden="true"><path d="M12 2a10 10 0 1 0 0 20 10 10 0 0 0 0-20zm0 2.2c1 0 2 .2 2.9.6l-1.4 1.6-2.3.3-.9 1.8-2.2-.3-1.3 1.7.7 2.3 2.2.6.8 2.3-.7 2.6 1 2.3A7.8 7.8 0 0 1 4.2 12c0-1.5.4-2.9 1.2-4.1l1.6.5 1.4-1.6A7.8 7.8 0 0 1 12 4.2zm6.2 3.1a7.8 7.8 0 0 1 .9 8.2l-1.6-1.3-.4-2.4-1.9-1.1.3-2.2z"/></svg>
        www.brambleworks.com.au
      </li>
    </ul>

    <address class="address">
      2346 First Address Line<br>
      Second Address Line, 56324
    </address>
  </section>
</main>
</body>
</html>
```